Website for Apartment Rental in Prague

I would like to create designs of my website focused on luxury apartment rentals in Prague, Czech Republic. I created initial mock-ups, They are all attached. I need to design homepage and subpage. The mock-ups were created by combining elements from different websites that I liked but I need you to create a design that is unique and original. The attached files a only a guidance for the structure of the website but not for the design. Try to be creative.

Industry/Entity Type

Apartment

```html
<!DOCTYPE html>
<html lang="en">
<head>
<meta charset="utf-8">
<title>Vltava Suites – Luxury Apartments</title>
<link href="https://fonts.googleapis.com/css2?family=Montserrat:wght@400;500;600;700&family=Lato:wght@300;400;700&display=swap" rel="stylesheet">
<style>
:root{
  --orange:#f4a95a;
  --orange-dark:#e8913a;
  --ink:#1c1c1c;
  --text:#555;
  --muted:#8a8a8a;
  --line:#e3e3e3;
  --cream:#fbf3ea;
  --panel:#f6f6f6;
  --footer:#f1f1f1;
  --white:#fff;
}
*{box-sizing:border-box;margin:0;padding:0}
html,body{width:1200px;height:4225px;overflow:hidden}
body{position:relative;background:var(--white);font-family:'Lato',sans-serif;color:var(--text)}
.abs{position:absolute}
/* top bar */
.topbar{left:0;top:0;width:1200px;height:100px;display:flex;align-items:center;justify-content:space-between;padding:0 79px;font-size:15px}
.topbar .links{color:var(--orange);letter-spacing:.5px;display:flex;gap:14px}
.topbar .links span.sep{color:#bbb}
.topbar .contact{display:flex;gap:26px;color:#555;font-size:14px;align-items:center}
.topbar .contact span{display:flex;align-items:center;gap:8px}
.brand{left:0;width:1200px;top:22px;text-align:center;font-family:'Montserrat',sans-serif;color:var(--ink)}
.brand .small{font-size:15px;letter-spacing:7px;color:#9a9a9a;font-weight:400}
.brand .big{font-size:34px;letter-spacing:8px;font-weight:600;line-height:1.1}
.brand .rule{width:180px;height:2px;background:var(--orange);margin:6px auto 0}
/* nav */
.nav{left:0;top:107px;width:1200px;height:52px;background:var(--cream);display:flex;align-items:center;padding-left:79px;gap:56px;font-family:'Montserrat',sans-serif;font-size:15px;color:var(--orange)}
.nav .active{color:var(--ink);border-bottom:2px solid var(--orange);padding-bottom:3px}
/* hero */
.hero{left:0;top:159px;width:1200px;height:517px;background:linear-gradient(100deg,#b07a3d 0%,#d7a467 22%,#c9b49a 40%,#a9c2d4 58%,#7fa2bf 78%,#c79a6a 100%)}
.booking{left:127px;top:473px;width:958px;height:152px;background:rgba(255,255,255,.86);padding:14px 16px;font-size:14px;color:#333}
.booking .row{display:flex;gap:12px;align-items:flex-end}
.field label{display:block;margin-bottom:5px}
.input{height:40px;background:var(--white);border:1px solid var(--line);padding:0 12px;display:flex;align-items:center;color:#aaa;font-size:14px}
.select{height:40px;width:54px;border:1px solid var(--line);background:var(--white);display:flex;align-items:center;justify-content:space-between;padding:0 8px;color:#333}
.btn-orange{background:var(--orange);color:var(--ink);height:40px;display:flex;align-items:center;justify-content:center;font-size:15px}
.official{left:79px;top:645px;width:1042px;height:68px;background:#111;color:var(--white);display:flex;align-items:center;padding-left:34px;font-family:'Montserrat',sans-serif;font-size:24px;font-weight:600;letter-spacing:1px}
.official small{font-size:18px;font-weight:400;margin-left:10px;letter-spacing:.5px}
.official .up{position:absolute;right:0;top:0;width:64px;height:68px;background:var(--orange);display:flex;align-items:center;justify-content:center}
/* headings */
.heading{left:0;width:1200px;text-align:center;font-family:'Montserrat',sans-serif;color:var(--ink)}
.heading h2{font-size:34px;font-weight:700;letter-spacing:1px;line-height:1.2}
.heading h2 span{font-size:26px;font-weight:500}
.heading .rule{width:200px;height:2px;background:var(--orange);margin:10px auto 0}
.lead{left:0;width:1200px;text-align:center;font-size:14px;line-height:1.7;color:#666}
/* interiors */
.interiors{left:0;top:972px;width:1200px;height:410px;background:linear-gradient(180deg,#fff 0%,#f3efe9 40%,#ece6de 70%,#fff 100%)}
.icon-circle{left:555px;top:988px;width:92px;height:92px;border-radius:50%;background:var(--white);box-shadow:0 4px 14px rgba(0,0,0,.12);display:flex;align-items:center;justify-content:center}
.interiors-title{left:0;top:1140px;width:1200px;text-align:center;font-family:'Montserrat',sans-serif;font-size:34px;font-weight:500;color:var(--ink)}
.interiors-text{left:160px;top:1210px;width:880px;text-align:center;font-size:15px;line-height:1.7;color:#555}
/* cards */
.card{width:332px;height:446px;background:var(--white);box-shadow:0 2px 10px rgba(0,0,0,.12);display:flex;flex-direction:column}
.card .photo{height:208px;position:relative}
.card .tag{position:absolute;left:8px;top:8px;background:var(--white);border:1px solid #ccc;padding:3px 14px;font-size:15px;color:#333}
.card .stats{display:flex;gap:28px;padding:18px 16px 0;font-size:14px;color:#666;align-items:center}
.card .stats span{display:flex;align-items:center;gap:6px}
.card .stats .area{margin-right:60px}
.card h3{font-family:'Lato',sans-serif;font-size:17px;font-weight:400;color:#222;padding:28px 20px 0;line-height:1.3}
.card p{font-size:14px;color:#777;padding:12px 20px 0;line-height:1.5}
.card .book{margin:auto auto 14px;width:186px;height:48px;border:1px solid #ccc;box-shadow:0 2px 4px rgba(0,0,0,.12);display:flex;align-items:center;justify-content:center;font-family:'Montserrat',sans-serif;font-size:17px;color:#222;background:var(--white)}
.card .book.hot{background:var(--orange);border-color:var(--orange)}
/* banner */
.banner{left:0;top:2558px;width:1200px;height:260px;background:linear-gradient(90deg,#2b2623 0%,#3d3530 45%,#1f1b19 100%);text-align:center;color:var(--white);font-family:'Montserrat',sans-serif}
.banner .big{font-size:104px;font-weight:500;letter-spacing:2px;padding-top:44px;line-height:1}
.banner .sub{font-size:44px;font-weight:500;margin-top:6px}
.banner .sub b{color:var(--orange);font-weight:600}
/* need to know */
.ph{border-radius:2px}
.step{width:84px;height:84px;border-radius:50%;background:var(--orange);color:var(--white);font-family:'Montserrat',sans-serif;font-size:34px;display:flex;align-items:center;justify-content:center}
.know-title{font-family:'Montserrat',sans-serif;font-size:32px;font-weight:600;color:var(--orange);letter-spacing:1px}
.know-text{font-size:15px;line-height:1.6;color:#444}
/* footer */
.footer{left:0;top:3930px;width:1200px;height:245px;background:var(--footer)}
.fcol{top:3970px}
.fcol h4{font-family:'Montserrat',sans-serif;font-size:18px;font-weight:600;color:var(--ink);margin-bottom:18px}
.fcol .item{display:flex;gap:10px;font-size:14px;color:#555;line-height:1.45;margin-bottom:12px}
.thumb{width:60px;height:52px;background:linear-gradient(135deg,#6a8fa9,#c9b89a);flex:none}
.tw-ico{width:30px;height:30px;border-radius:50%;background:var(--orange);flex:none}
.meta{font-size:12px;color:#888;margin-top:3px}
.copyright{left:0;top:4175px;width:1200px;height:50px;background:var(--orange-dark);color:var(--white);text-align:center;line-height:50px;font-size:15px}
.copyright b{font-family:'Montserrat',sans-serif;letter-spacing:1px}
</style>
</head>
<body>

<header>
  <div class="abs topbar">
    <div class="links"><span>DISCOVER PRAGUE</span><span class="sep">/</span><span>OUR HOSPITALITY</span><span class="sep">/</span><span style="color:#333">EN ▾</span></div>
    <div class="contact">
      <span><svg width="16" height="12" viewBox="0 0 16 12"><rect width="16" height="12" rx="1" fill="#333"/><path d="M1 1l7 6 7-6" stroke="#fff" fill="none"/></svg>reservation@vltavasuites.cz</span>
      <span><svg width="14" height="14" viewBox="0 0 24 24"><path d="M6.6 10.8a15 15 0 006.6 6.6l2.2-2.2a1 1 0 011-.25 11.4 11.4 0 003.6.57 1 1 0 011 1V20a1 1 0 01-1 1A17 17 0 013 4a1 1 0 011-1h3.5a1 1 0 011 1 11.4 11.4 0 00.57 3.6 1 1 0 01-.25 1z" fill="#333"/></svg>+420 600 481 263</span>
    </div>
  </div>
  <div class="abs brand">
    <div class="small">VLTAVA</div>
    <div class="big">SUITES</div>
    <div class="rule"></div>
  </div>
  <nav class="abs nav">
    <span class="active">HOME</span><span>APARTMENTS</span><span>SERVICES</span><span>GALLERY</span><span>NEWS</span><span>EXCLUSIVE OFFERS &amp; TOURS</span><span>FOR FAMILIES</span><span>CONTACT US</span>
  </nav>
</header>

<section>
  <div class="abs hero" role="img" aria-label="Photo of a sunlit apartment terrace with sofa and cushions overlooking a river and city skyline"></div>
  <form class="abs booking">
    <div class="row">
      <div class="field"><label>Check in date</label><div class="input" style="width:354px">11/17/2017</div></div>
      <div class="field"><label>Check out date</label><div class="input" style="width:354px">11/18/2017</div></div>
      <div class="field"><label>Adults</label><div class="select">2 <span>▾</span></div></div>
      <div class="field"><label>Children</label><div class="select">0 <span>▾</span></div></div>
      <div class="field"><label>Infants</label><div class="select">0 <span>▾</span></div></div>
    </div>
    <div class="row" style="margin-top:10px">
      <div class="field"><label>Promotional code</label><div class="input" style="width:415px"></div></div>
      <div class="btn-orange" style="width:150px">Check availability</div>
      <div style="height:40px;line-height:40px;padding:0 4px">Or</div>
      <div class="btn-orange" style="width:287px;justify-content:space-between;padding:0 12px;font-size:14px">Select Rental Unit <span>▾</span></div>
    </div>
  </form>
  <div class="abs official">OFFICIAL SITE - <small>BEST PRICE GUARANTEED</small>
    <div class="up"><svg width="18" height="18" viewBox="0 0 18 18"><path d="M3 9l6-6 6 6M3 15l6-6 6 6" stroke="#111" stroke-width="2.4" fill="none"/></svg></div>
  </div>
</section>

<section>
  <div class="abs heading" style="top:758px"><h2>A DIFFERENT VISION</h2><h2>OF <span>TRAVELLING</span></h2><div class="rule" style="width:150px"></div></div>
  <p class="abs lead" style="top:866px">Something spectacular has arrived in the heart of Europe.<br>Steps from Old Town, this rental experience is curated with world-class amenities, exemplary style and a level of convenience you have to experience to belive.<br>Experience the different vision of luxury in center of Prague.</p>
</section>

<section>
  <div class="abs interiors" role="img" aria-label="Faint photo of an elegant living room interior"></div>
  <div class="abs icon-circle"><svg width="40" height="40" viewBox="0 0 40 40"><rect x="3" y="3" width="34" height="34" rx="4" fill="none" stroke="#e8913a" stroke-width="2"/><path d="M10 20l10-8 10 8M13 18v11h14V18" fill="none" stroke="#e8913a" stroke-width="2"/><circle cx="20" cy="23" r="2.5" fill="#e8913a"/></svg></div>
  <h2 class="abs interiors-title">Interiors Designed by Maison Lumen</h2>
  <p class="abs interiors-text">Maison Lumen apartments offers short term and as well as long term options in our studio apartments and our one bedroom apartment homes. Our luxurious apartments and high quality customer services have allowed us to domainate tha prague apartment market with a proven track record. Our years of experience and knowledge have made us a premier apartment rental company as we continue to stress the importance of servicing individuals and corporations who are seeking the finestaccommodations.</p>
</section>

<section>
  <div class="abs heading" style="top:1437px"><h2>EXCLUSIVE OFFERS</h2><h2>AND <span>TOURS</span></h2><div class="rule" style="width:150px"></div></div>
  <p class="abs lead" style="top:1540px">Something spectacular has arrived in the heart of Europe.</p>

  <article class="abs card" style="left:79px;top:1583px">
    <div class="photo" role="img" aria-label="Photo of a modern white living room with fireplace" style="background:linear-gradient(135deg,#d9d6d1,#8a8580)"><span class="tag">Rent</span></div>
    <div class="stats"><span class="area">✛ 250 sqft</span><span>▭ 3</span><span>◡ 2</span></div>
    <h3>Brand New Modern Apartment<br>Unbeatable Location</h3>
    <p>Lorem Ipsum has been the industry's standard dummy text ever since the 1500.</p>
    <div class="book hot">BOOK NOW</div>
  </article>
  <article class="abs card" style="left:434px;top:1583px">
    <div class="photo" role="img" aria-label="Photo of a warm-toned open living and dining room" style="background:linear-gradient(135deg,#c9a37c,#6e5a48)"><span class="tag">Rent</span></div>
    <div class="stats"><span class="area">✛ 250 sqft</span><span>▭ 3</span><span>◡ 2</span></div>
    <h3>Brand New Modern Apartment<br>Unbeatable Location</h3>
    <p>Lorem Ipsum has been the industry's standard dummy text ever since the 1500.</p>
    <div class="book">BOOK NOW</div>
  </article>
  <article class="abs card" style="left:789px;top:1583px">
    <div class="photo" role="img" aria-label="Photo of a bright minimalist lounge" style="background:linear-gradient(135deg,#efece7,#b9b1a6)"><span class="tag">Rent</span></div>
    <div class="stats"><span class="area">✛ 250 sqft</span><span>▭ 3</span><span>◡ 2</span></div>
    <h3>Brand New Modern Apartment<br>Unbeatable Location</h3>
    <p>Lorem Ipsum has been the industry's standard dummy text ever since the 1500.</p>
    <div class="book">BOOK NOW</div>
  </article>

  <article class="abs card" style="left:79px;top:2056px">
    <div class="photo" role="img" aria-label="Photo of a white living room with bookshelves" style="background:linear-gradient(135deg,#ebe9e5,#9c978f)"><span class="tag">Rent</span></div>
    <div class="stats"><span class="area">✛ 250 sqft</span><span>▭ 3</span><span>◡ 2</span></div>
    <h3>Brand New Modern Apartment<br>Unbeatable Location</h3>
    <p>Lorem Ipsum has been the industry's standard dummy text ever since the 1500.</p>
    <div class="book">BOOK NOW</div>
  </article>
  <article class="abs card" style="left:434px;top:2056px">
    <div class="photo" role="img" aria-label="Photo of a living room with an indoor garden" style="background:linear-gradient(135deg,#dcd8d0,#7f9a6d)"><span class="tag">Rent</span></div>
    <div class="stats"><span class="area">✛ 250 sqft</span><span>▭ 3</span><span>◡ 2</span></div>
    <h3>Brand New Modern Apartment<br>Unbeatable Location</h3>
    <p>Lorem Ipsum has been the industry's standard dummy text ever since the 1500.</p>
    <div class="book">BOOK NOW</div>
  </article>
  <article class="abs card" style="left:789px;top:2056px">
    <div class="photo" role="img" aria-label="Photo of a bedroom with orange bedding" style="background:linear-gradient(135deg,#d99a4e,#8a4a1f)"><span class="tag">Rent</span></div>
    <div class="stats"><span class="area">✛ 250 sqft</span><span>▭ 3</span><span>◡ 2</span></div>
    <h3>Brand New Modern Apartment<br>Unbeatable Location</h3>
    <p>Lorem Ipsum has been the industry's standard dummy text ever since the 1500.</p>
    <div class="book">BOOK NOW</div>
  </article>
</section>

<section class="abs banner" role="img" aria-label="Dark photo of an apartment interior behind the booking call to action">
  <div class="big">BOOKING</div>
  <div class="sub">A Home <b>Online ›</b></div>
</section>

<section>
  <div class="abs heading" style="top:2866px"><h2 style="font-size:32px">NEED TO KNOW</h2></div>
  <p class="abs lead" style="top:2930px">Maison Lumen apartments offers short term and as well as long term options in our studio apartments.</p>

  <div class="abs ph" style="left:0;top:2991px;width:520px;height:333px;background:linear-gradient(135deg,#f4f4f4 5%,#b7634a 40%,#9a4e3a 65%,#f4f4f4 95%)" role="img" aria-label="Photo of a red-brick modern apartment building"></div>
  <svg class="abs" style="left:420px;top:3028px" width="240" height="700" viewBox="0 0 240 700">
    <path d="M180 0 C290 90 280 250 180 330 C70 400 70 600 180 679" fill="none" stroke="#d5d5d5" stroke-width="2"/>
  </svg>
  <div class="abs step" style="left:558px;top:2986px">1</div>
  <div class="abs step" style="left:558px;top:3316px">2</div>
  <div class="abs step" style="left:558px;top:3665px">3</div>

  <div class="abs" style="left:727px;top:3000px">
    <div class="know-title">APARTMENTS :</div>
    <p class="know-text" style="margin-top:8px">also available to rent all the apartments<br>together for companies or larger groups.</p>
  </div>
  <div class="abs ph" style="left:900px;top:3127px;width:300px;height:535px;background:linear-gradient(180deg,#f5f2ee,#e6d9cc 50%,#fff)" role="img" aria-label="Photo of a smiling couple at an apartment door"></div>

  <div class="abs" style="left:79px;top:3340px;width:366px">
    <div class="know-title">CHECK-OUT :</div>
    <p class="know-text" style="margin-top:8px;text-align:right">12 noon; earliest check-in, 3pm- both are flexible,<br>by arrangement.</p>
  </div>
  <div class="abs ph" style="left:0;top:3521px;width:535px;height:339px;background:linear-gradient(160deg,#fff 10%,#e3c6ad 45%,#b8c4a6 70%,#fff 95%)" role="img" aria-label="Photo of a hand holding banknotes"></div>

  <div class="abs" style="left:727px;top:3680px">
    <div class="know-title">RATES :</div>
    <p class="know-text" style="margin-top:8px">prices from 150 USD per night,<br>including tax.</p>
  </div>
</section>

<footer>
  <div class="abs footer"></div>
  <div class="abs fcol" style="left:79px;width:240px">
    <h4>CONTACT INFO</h4>
    <div class="item"><svg width="16" height="20" viewBox="0 0 16 20"><path d="M8 0a7 7 0 00-7 7c0 5 7 13 7 13s7-8 7-13a7 7 0 00-7-7z" fill="#f4a95a"/><circle cx="8" cy="7" r="2.5" fill="#fff"/></svg><span>123 Lorem ipsum dummy text,<br>Country-123456.</span></div>
    <div class="item"><svg width="16" height="16" viewBox="0 0 24 24"><path d="M6.6 10.8a15 15 0 006.6 6.6l2.2-2.2a1 1 0 011-.25 11.4 11.4 0 003.6.57 1 1 0 011 1V20a1 1 0 01-1 1A17 17 0 013 4a1 1 0 011-1h3.5a1 1 0 011 1 11.4 11.4 0 00.57 3.6 1 1 0 01-.25 1z" fill="#f4a95a"/></svg><span>+420 600 481 263</span></div>
    <div class="item"><svg width="16" height="12" viewBox="0 0 16 12"><rect width="16" height="12" rx="1" fill="#f4a95a"/><path d="M1 1l7 6 7-6" stroke="#fff" fill="none"/></svg><span>reservation@vltavasuites.cz</span></div>
  </div>
  <div class="abs fcol" style="left:344px;width:240px">
    <h4>LATEST NEWS</h4>
    <div class="item"><div class="thumb" role="img" aria-label="News thumbnail photo"></div><div>Lorem Ipsum is simply<br>dummy text of<div class="meta">♡ 15 Likes &nbsp; ↗ Share</div></div></div>
    <div class="item"><div class="thumb" role="img" aria-label="News thumbnail photo"></div><div>Lorem Ipsum is simply<br>dummy text of<div class="meta">♡ 15 Likes &nbsp; ↗ Share</div></div></div>
  </div>
  <div class="abs fcol" style="left:608px;width:250px">
    <h4>TWEETER FEED</h4>
    <div class="item"><div class="tw-ico"></div><div style="font-size:12px;line-height:1.4"><b style="color:#333">reservation</b> <span style="float:right;color:#333;font-weight:700">3 HRS.</span><br>@vltavasuites<br>#WeekendayWisdom Always call a register tourist for any #Place.</div></div>
    <div class="item"><div class="tw-ico"></div><div style="font-size:12px;line-height:1.4"><b style="color:#333">reservation</b> <span style="float:right;color:#333;font-weight:700">3 HRS.</span><br>@vltavasuites<br>#WeekendayWisdom Always call a register tourist for any #Place.</div></div>
  </div>
  <div class="abs fcol" style="left:873px;width:248px">
    <h4>GALLERY</h4>
    <div style="display:grid;grid-template-columns:repeat(3,80px);gap:4px" role="img" aria-label="Grid of apartment and city photos">
      <div style="height:68px;background:#8c7762"></div><div style="height:68px;background:#5f7d99"></div><div style="height:68px;background:#b39a7d"></div>
      <div style="height:68px;background:#6d6a66"></div><div style="height:68px;background:#c7a27a"></div><div style="height:68px;background:#7b8f9f"></div>
    </div>
  </div>
  <div class="abs copyright">© <b>VLTAVA SUITES</b> - 2017, All Rights Reserved</div>
</footer>

</body>
</html>
```